Maplerise Trading Inc. needs an innovative idea for letterhead and visiting cards.

Maplerise Trading Inc. is a Canadian brand since 2007. It is a renown dealer of kids and office furniture locally. Moreover, exporting electric fixtures e.g. switches, LED's, down-lights etc. to Middle East and Africa. We have initiated a number of steps including re-branding, to boost our export in 2020. We have successfully designed our new logo a few months ago through 'Artfolio' and now we are looking for an innovative idea for a letterhead.
Some key points:
• Red, black and white are the three colors used in all our packaging and furniture. (grey is optional)
• Shouldn’t be too wide.
• Use of watermark is preferable.
• You can visit our North American site at www.mapleriseinc.com. Export website of the company will be launched soon. www.mapleriseinc.ca
• Same letterhead will be used locally and internationally.
• Our new logo and sample packaging is attached.

```html
<!DOCTYPE html>
<html lang="en">
<head>
<meta charset="utf-8">
<title>Maplerise Trading – Business Card</title>
<link href="https://fonts.googleapis.com/css2?family=Montserrat:wght@400;500;600;700&display=swap" rel="stylesheet">
<style>
  :root {
    --backdrop: #1b1c1f;
    --card: #2a2b2f;
    --card-mark: #313236;
    --red: #c1212b;
    --white: #f4f4f4;
    --grey: #b9babd;
    --black: #111214;
  }
  * { margin: 0; padding: 0; box-sizing: border-box; }
  html, body { width: 1200px; height: 800px; overflow: hidden; }
  body {
    background: var(--backdrop);
    font-family: "Montserrat", Arial, sans-serif;
    display: flex; align-items: center; justify-content: center; gap: 48px;
  }
  .card {
    position: relative; width: 525px; height: 300px;
    background: var(--card); border-radius: 16px; overflow: hidden;
  }
  .card__mark {
    position: absolute; width: 190px; height: 190px;
    background: var(--card-mark); border-radius: 10px;
  }
  .card--front .card__mark { left: 300px; top: 90px; }
  .card--back .card__mark { left: 320px; top: 30px; }

  .brand { position: absolute; display: flex; align-items: center; gap: 14px; }
  .brand__square { width: 44px; height: 44px; border-radius: 6px; }
  .brand__name { font-weight: 600; letter-spacing: 1px; font-size: 26px; }
  .card--front .brand { left: 50%; top: 50%; transform: translate(-50%, -50%); }
  .card--front .brand__square { background: var(--black); }
  .card--front .brand__name { color: var(--black); }
  .card--back .brand { left: 34px; top: 40px; }
  .card--back .brand__square { background: var(--red); }
  .card--back .brand__name { color: var(--white); }

  .person { position: absolute; left: 34px; top: 130px; }
  .person__name { color: var(--white); font-weight: 700; font-size: 19px; letter-spacing: 1px; }
  .person__role { color: var(--red); font-weight: 500; font-size: 13px; margin-top: 2px; }
  .divider { position: absolute; left: 34px; right: 34px; top: 183px; height: 1px; background: var(--red); }

  .contacts {
    position: absolute; left: 34px; right: 34px; top: 198px;
    display: grid; grid-template-columns: auto auto auto; column-gap: 26px;
    color: var(--grey); font-size: 11px; line-height: 20px;
  }
  .contacts__label { color: var(--red); font-weight: 700; margin-right: 4px; }
  .contacts__icon { width: 9px; height: 9px; margin-right: 6px; vertical-align: -1px; }
  .card__band { position: absolute; left: 0; right: 0; bottom: 0; height: 12px; background: var(--red); }
</style>
</head>
<body>
  <section class="card card--front" aria-label="Card front">
    <div class="card__mark"></div>
    <div class="brand">
      <span class="brand__square"></span>
      <span class="brand__name">MAPLERISE TRADING</span>
    </div>
  </section>

  <section class="card card--back" aria-label="Card back">
    <div class="card__mark"></div>
    <div class="brand">
      <span class="brand__square"></span>
      <span class="brand__name">MAPLERISE TRADING</span>
    </div>
    <div class="person">
      <p class="person__name">DANIEL WHITFORD</p>
      <p class="person__role">Manager</p>
    </div>
    <div class="divider"></div>
    <div class="contacts">
      <div>
        <p><span class="contacts__label">CA:</span>(888) 555-0142</p>
        <p><span class="contacts__label">US:</span>(929) 555-0187</p>
      </div>
      <div>
        <p><svg class="contacts__icon" viewBox="0 0 10 10"><rect x="0.5" y="1.5" width="9" height="7" fill="none" stroke="#c1212b"/><path d="M0.5 1.5 L5 5.5 L9.5 1.5" fill="none" stroke="#c1212b"/></svg>info@mapleriseinc.com</p>
        <p><svg class="contacts__icon" viewBox="0 0 10 10"><circle cx="5" cy="5" r="4.5" fill="none" stroke="#c1212b"/><path d="M0.5 5 H9.5 M5 0.5 V9.5" stroke="#c1212b"/></svg>www.mapleriseinc.com</p>
      </div>
      <div>
        <p>48 Harbourview Rd, Unit 210</p>
        <p>Markham, ON L3R 2K7</p>
      </div>
    </div>
    <div class="card__band"></div>
  </section>
</body>
</html>
```